Eco-Friendly Wheat Straw Drinking Straw Packaging Design Contest

We are seeking talented designers to create a standout packaging design for our eco-friendly wheat straw drinking straws. Our product is an environmentally conscious alternative to plastic and paper straws. We want a design that not only reflects our brand values of sustainability and health but also stands out on store shelves. Please see attached file for detailed brief and requirements.
Updates

Colors
00AB8E
00BBA5
67D7C9
C6EFE9
E9F9F6
59FF00
82FF00
B8FF75
E3FFCB
F4FFEA
FFF300
FFF600
FEFA6F
FFFEC7
FFFEE8

Requirements
Must have
• Clean, modern, and visually appealing design focusing on eco-friendliness and health. Use of earthy colors like green, beige, or brown. Final design should be in Turkish. Please see the brief file attached for further details.
Nice to have
• Scalable design that can be adapted for various packaging sizes. Incorporate creative illustrations or graphics representing wheat, nature, or sustainability.
Should not have
• Avoid overly complex or cluttered designs. Simplicity and clarity are key. Do not use bright or flashy colors that do not align with the natural and eco-friendly theme of the product. Avoid using English text in the final design. All text should be in Turkish, as the product will be marketed locally.

```html
<!DOCTYPE html>
<html lang="tr">
<head>
<meta charset="UTF-8">
<title>Doğal Buğday Sapından Pipet – Etiket</title>
<link href="https://fonts.googleapis.com/css2?family=Quicksand:wght@700&family=Fredoka:wght@500&family=Open+Sans:wght@600;700&display=swap" rel="stylesheet">
<style>
  :root {
    --page-bg: #f4f3ef;
    --peach: #e0a98a;
    --peach-text: #d99c7c;
    --peach-line: #d8b2a0;
    --sage: #c3cfc0;
    --card: #ffffff;
    --green: #3b9f53;
    --ink: #2b2b2b;
    --wheat-light: #b8c3b3;
    --wheat-dark: #a3ae9f;
  }
  * { margin: 0; padding: 0; box-sizing: border-box; }
  html, body { width: 900px; height: 1200px; overflow: hidden; background: var(--page-bg); }
  .label {
    position: absolute; left: 40px; top: 130px; width: 820px; height: 940px;
    background: linear-gradient(to bottom, var(--peach) 0, var(--peach) 57.5%, var(--sage) 57.5%, var(--sage) 100%);
  }
  .wheat-art {
    position: absolute; left: 330px; top: 680px; width: 440px; height: 260px;
    background: linear-gradient(to top, var(--wheat-dark) 0%, var(--wheat-light) 55%, rgba(195,207,192,0) 100%);
    opacity: .7;
  }
  .info-card {
    position: absolute; left: 126px; top: 120px; width: 586px; height: 556px;
    background: var(--card); border-radius: 26px;
    border: 3px solid var(--peach-line);
    box-shadow: 0 0 0 7px var(--card);
    text-align: center; padding-top: 62px;
  }
  .brand-name {
    font-family: "Quicksand", sans-serif; font-weight: 700; color: var(--green);
    font-size: 52px; line-height: 1; letter-spacing: 1px;
  }
  .product-title {
    font-family: "Quicksand", sans-serif; font-weight: 700; color: var(--green);
    font-size: 37px; line-height: 1.3; margin-top: 52px;
  }
  .slogan {
    font-family: "Fredoka", sans-serif; font-weight: 500; color: var(--peach-text);
    font-size: 39px; line-height: 1.25; margin-top: 14px; letter-spacing: .5px;
  }
  .features {
    list-style: none; font-family: "Open Sans", sans-serif; font-weight: 600;
    color: var(--peach-text); font-size: 21px; line-height: 1.42; margin-top: 14px;
  }
  .pack-info {
    position: absolute; left: 64px; top: 822px;
    font-family: "Quicksand", sans-serif; font-weight: 700; color: var(--ink);
    font-size: 32px; line-height: 1.05;
  }
  .pack-info .note { font-family: "Open Sans", sans-serif; font-size: 19px; margin-top: 6px; }
</style>
</head>
<body>
  <div class="label">
    <div class="wheat-art" role="img" aria-label="Buğday başakları illüstrasyonu"></div>
    <div class="info-card">
      <div class="brand-name">HASATLI</div>
      <h1 class="product-title">Doğal Buğday Sapından<br>Pipet</h1>
      <p class="slogan">Topraktan Masaya,<br>Masadan Toprağa!</p>
      <ul class="features">
        <li>Doğada çözünür</li>
        <li>Sıvı içerisinde erimez, yumuşamaz</li>
        <li>Kimyasal içermez</li>
        <li>Gıda ile temasa uygundur</li>
      </ul>
    </div>
    <div class="pack-info">
      <div>15 cm</div>
      <div>500 adet</div>
      <div class="note">Tek kullanimliktir.</div>
    </div>
  </div>
</body>
</html>
```